Blue Harbor Business Cards

Name Tomas Welbridge
Title Mortgage Originator
Phone (800) 614-2290 x32
Direct (571) 362-0471
Email twelbridge@blueharborhomeloans.com
NMLS #1847362
Name Lena Ortiz
Title Mortgage Originator
Location (800) 614-2290 x55
Direct (440) 276-5190
Email lortiz@blueharborhomeloans.com
NMLS #2739418
Name Desmond Holloway-Finch
Title Mortgage Originator
Location (800) 614-2290 x56
Direct (202) 634-1975
Email dhollowayfinch@blueharborhomeloans.com
NMLS #2784530
Name Rosalyn Whitaker
Title Mortgage Originator
Location (800) 614-2290 x57
Direct (240) 358-6621
Email rwhitaker@blueharborhomeloans.com
NMLS #2491086
Name Gwen Holbrook
Title Mortgage Originator
Location (800) 614-2290 x58
Direct (540) 716-2384
Email gholbrook@blueharborhomeloans.com
NMLS #2438617
Name Ravi Dunmore
Title Mortgage Originator
Location (800) 614-2290 x59
Direct (240) 563-8827
Email rdunmore@blueharborhomeloans.com
NMLS #2597142
Name Ivy Marlow
Title Mortgage Originator
Location (800) 614-2290 x60
Direct (202) 479-3306
Email ivy@ivyfindshomes.com
NMLS #2718394
Contact Information for Business Card
Name Tomas Welbridge Title Mortgage Originator Phone (800) 614-2290 x32 Direct (571) 362-0471 Email twelbridge@blueharborhomeloans.com NMLS #1847362 Name Lena Ortiz Title Mortgage Originator Location (800) 614-2290 x55 Direct (440) 276-5190 Email lortiz@blueharborhomeloans.com NMLS #2739418 Name Desmond Holloway-Finch Title Mortgage Originator Location (800) 614-2290 x56 Direct (202) 634-1975 Email dhollowayfinch@blueharborhomeloans.com NMLS #2784530 Name Rosalyn Whitaker Title Mortgage Originator Location (800) 614-2290 x57 Direct (240) 358-6621 Email rwhitaker@blueharborhomeloans.com NMLS #2491086 Name Gwen Holbrook Title Mortgage Originator Location (800) 614-2290 x58 Direct (540) 716-2384 Email gholbrook@blueharborhomeloans.com NMLS #2438617 Name Ravi Dunmore Title Mortgage Originator Location (800) 614-2290 x59 Direct (240) 563-8827 Email rdunmore@blueharborhomeloans.com NMLS #2597142 Name Ivy Marlow Title Mortgage Originator Location (800) 614-2290 x60 Direct (202) 479-3306 Email ivy@ivyfindshomes.com NMLS #2718394
Look and feel
Each slider illustrates characteristics of the customer's brand and the style your logo design should communicate.

```html
<!DOCTYPE html>
<html lang="en">
<head>
<meta charset="utf-8">
<title>Blue Harbor Business Card</title>
<link href="https://fonts.googleapis.com/css2?family=Titillium+Web:wght@400;600;700&display=swap" rel="stylesheet">
<style>
:root{
  --navy:#08171d;
  --gold:#d9a441;
  --gold-light:#f0c465;
  --orange:#f5a020;
  --blue-deep:#2b3f93;
  --blue-mid:#4a7bc4;
  --blue-wash:#5d80bd;
  --white:#ffffff;
  --page:#ffffff;
}
*{margin:0;padding:0;box-sizing:border-box}
html,body{width:960px;height:1200px;overflow:hidden;background:var(--page)}
body{position:relative;font-family:'Titillium Web',sans-serif;color:var(--white)}
.card{position:absolute;left:94px;width:796px;height:461px;overflow:hidden}
.card-front{top:84px;background:var(--navy)}
.card-back{top:638px}

.brand{position:absolute;left:41px;top:96px;width:293px;display:flex;align-items:center;gap:12px}
.brand-dot{width:22px;height:22px;border-radius:50%;background:var(--gold);flex:none}
.brand-name{font-weight:700;font-size:30px;color:var(--gold);line-height:1}

.identity{position:absolute;right:31px;top:26px;text-align:right}
.identity-name{font-weight:700;font-size:31px;line-height:1.1;color:var(--gold)}
.identity-line{font-size:20px;line-height:28px;font-weight:400}

.portrait{position:absolute;left:472px;top:118px;width:324px;height:300px;
  border-radius:150px 150px 0 0;
  background:radial-gradient(ellipse at 45% 35%,#b0703a 0%,#7a4522 40%,#2a2a35 75%,var(--navy) 100%)}

.contacts{position:absolute;left:40px;top:240px;list-style:none}
.contacts li{display:flex;align-items:center;height:28.5px;font-size:21px;font-weight:400}
.contacts svg{width:20px;height:20px;margin-right:9px;flex:none}

.footer-band{position:absolute;left:0;bottom:0;width:796px;height:110px}
.address{position:absolute;left:0;right:0;bottom:20px;text-align:center;font-size:23px;font-weight:600;letter-spacing:.3px}

.backdrop{position:absolute;inset:0;
  background:linear-gradient(120deg,#6a8cc6 0%,var(--blue-wash) 45%,#4f73b3 100%)}
.programs{position:absolute;left:36px;width:700px}
.programs-title{margin-left:33px;font-size:24px;font-weight:700;color:var(--orange);line-height:28px}
.programs ul{list-style:none}
.programs li{display:flex;align-items:center;font-size:20px;font-weight:400;line-height:25px}
.tick{width:26px;height:22px;margin-right:7px;flex:none}
.group-traditional{top:31px}
.group-low-credit{top:172px}
.group-alternative{top:308px}
</style>
</head>
<body>

<section class="card card-front">
  <div class="brand">
    <span class="brand-dot"></span>
    <span class="brand-name">Blue Harbor</span>
  </div>

  <div class="identity">
    <div class="identity-name">Ravi Dunmore</div>
    <div class="identity-line">Mortgage Originator</div>
    <div class="identity-line">NMLS #2597142</div>
  </div>

  <div class="portrait" role="img" aria-label="Portrait photo of the loan originator"></div>

  <ul class="contacts">
    <li><svg viewBox="0 0 20 20"><rect x="5" y="1" width="10" height="18" rx="2" fill="none" stroke="var(--gold)" stroke-width="2"/><rect x="8" y="15" width="4" height="1.6" fill="var(--gold)"/></svg>(240) 563-8827</li>
    <li><svg viewBox="0 0 20 20"><path d="M2 7c0-3 3-4 8-4s8 1 8 4l-3 1-1-2H6L5 8z" fill="var(--gold)"/><path d="M5 9h10l2 7H3z" fill="var(--gold)"/></svg>(800) 614-2290 x59</li>
    <li><svg viewBox="0 0 20 20"><rect x="1.5" y="4" width="17" height="12" fill="none" stroke="var(--gold)" stroke-width="2"/><path d="M2 5l8 6 8-6" fill="none" stroke="var(--gold)" stroke-width="2"/></svg>rdunmore@blueharborhomeloans.com</li>
    <li><svg viewBox="0 0 20 20" fill="none" stroke="var(--gold)" stroke-width="1.6"><circle cx="10" cy="10" r="8.5"/><ellipse cx="10" cy="10" rx="4" ry="8.5"/><path d="M1.5 10h17M3 5.5h14M3 14.5h14"/></svg>www.blueharborhomeloans.com</li>
  </ul>

  <svg class="footer-band" viewBox="0 0 796 110" preserveAspectRatio="none">
    <defs>
      <linearGradient id="goldFade" x1="0" x2="1">
        <stop offset="0" stop-color="var(--gold)"/>
        <stop offset="1" stop-color="var(--gold-light)"/>
      </linearGradient>
      <linearGradient id="blueBand" x1="0" y1="1" x2="1" y2="0">
        <stop offset="0" stop-color="var(--blue-deep)"/>
        <stop offset="1" stop-color="var(--blue-mid)"/>
      </linearGradient>
    </defs>
    <path d="M0 6 C200 30 500 50 796 42 L796 110 L0 110Z" fill="url(#goldFade)"/>
    <path d="M0 34 C250 50 550 52 796 30 L796 110 L0 110Z" fill="url(#blueBand)"/>
  </svg>
  <div class="address">2800 Harborview Lane Columbia, MD 21044</div>
</section>

<section class="card card-back">
  <div class="backdrop" role="img" aria-label="Soft blue-tinted photo of a smiling family of four"></div>

  <div class="programs group-traditional">
    <div class="programs-title">Traditional Loan Programs</div>
    <ul>
      <li><svg class="tick" viewBox="0 0 26 22"><rect x="1" y="6" width="15" height="15" fill="none" stroke="var(--orange)" stroke-width="1.5"/><path d="M4 12l5 5L24 2" fill="none" stroke="var(--orange)" stroke-width="3.5"/></svg>FHA loans starting at 500 score</li>
      <li><svg class="tick" viewBox="0 0 26 22"><rect x="1" y="6" width="15" height="15" fill="none" stroke="var(--orange)" stroke-width="1.5"/><path d="M4 12l5 5L24 2" fill="none" stroke="var(--orange)" stroke-width="3.5"/></svg>FHA 203K starting at 600 score</li>
      <li><svg class="tick" viewBox="0 0 26 22"><rect x="1" y="6" width="15" height="15" fill="none" stroke="var(--orange)" stroke-width="1.5"/><path d="M4 12l5 5L24 2" fill="none" stroke="var(--orange)" stroke-width="3.5"/></svg>VA loans starting at 580 score</li>
      <li><svg class="tick" viewBox="0 0 26 22"><rect x="1" y="6" width="15" height="15" fill="none" stroke="var(--orange)" stroke-width="1.5"/><path d="M4 12l5 5L24 2" fill="none" stroke="var(--orange)" stroke-width="3.5"/></svg>All Conventional loan programs</li>
    </ul>
  </div>

  <div class="programs group-low-credit">
    <div class="programs-title">Low Credit Score Programs</div>
    <ul>
      <li><svg class="tick" viewBox="0 0 26 22"><rect x="1" y="6" width="15" height="15" fill="none" stroke="var(--orange)" stroke-width="1.5"/><path d="M4 12l5 5L24 2" fill="none" stroke="var(--orange)" stroke-width="3.5"/></svg>500 score up to 90% LTV (FHA)</li>
      <li><svg class="tick" viewBox="0 0 26 22"><rect x="1" y="6" width="15" height="15" fill="none" stroke="var(--orange)" stroke-width="1.5"/><path d="M4 12l5 5L24 2" fill="none" stroke="var(--orange)" stroke-width="3.5"/></svg>540 score up to 75% LTV (Non-QM)</li>
      <li><svg class="tick" viewBox="0 0 26 22"><rect x="1" y="6" width="15" height="15" fill="none" stroke="var(--orange)" stroke-width="1.5"/><path d="M4 12l5 5L24 2" fill="none" stroke="var(--orange)" stroke-width="3.5"/></svg>580 score up to 96.5% LTV (FHA)</li>
      <li><svg class="tick" viewBox="0 0 26 22"><rect x="1" y="6" width="15" height="15" fill="none" stroke="var(--orange)" stroke-width="1.5"/><path d="M4 12l5 5L24 2" fill="none" stroke="var(--orange)" stroke-width="3.5"/></svg>580 score up to 100% LTV (VA)</li>
    </ul>
  </div>

  <div class="programs group-alternative">
    <div class="programs-title">Alternative Loan Programs</div>
    <ul>
      <li><svg class="tick" viewBox="0 0 26 22"><rect x="1" y="6" width="15" height="15" fill="none" stroke="var(--orange)" stroke-width="1.5"/><path d="M4 12l5 5L24 2" fill="none" stroke="var(--orange)" stroke-width="3.5"/></svg>Debt Service Coverage Ratio (DSCR) loans up to 85% LTV</li>
      <li><svg class="tick" viewBox="0 0 26 22"><rect x="1" y="6" width="15" height="15" fill="none" stroke="var(--orange)" stroke-width="1.5"/><path d="M4 12l5 5L24 2" fill="none" stroke="var(--orange)" stroke-width="3.5"/></svg>Investor Fix &amp; Flip Loans</li>
      <li><svg class="tick" viewBox="0 0 26 22"><rect x="1" y="6" width="15" height="15" fill="none" stroke="var(--orange)" stroke-width="1.5"/><path d="M4 12l5 5L24 2" fill="none" stroke="var(--orange)" stroke-width="3.5"/></svg>HELOC's and HELOAN's up to 95% LTV</li>
      <li><svg class="tick" viewBox="0 0 26 22"><rect x="1" y="6" width="15" height="15" fill="none" stroke="var(--orange)" stroke-width="1.5"/><path d="M4 12l5 5L24 2" fill="none" stroke="var(--orange)" stroke-width="3.5"/></svg>Foreign National Loans</li>
    </ul>
  </div>
</section>

</body>
</html>
```